Super elegant, crisp & clean Business card design required

We recently upgraded our branding - which is on our website - tavorelstudio.com

I would like a simple, yet elegant, clean business card design please.

The font of my logo is Cinzel - and because of the natural colour - it's best to have this on a black background.

I would like to have the back of the business card - with simply my logo.

PLEASE DO NOT SUBMIT A COMPLICATED / UNCLEAN DESIGN

Industry/Entity Type

Business

Contact Information for Business Card

Dalvik Ostrander Photography

Font styles to use
Other font styles liked:
• Cinzel

Requirements
Must have
• A backpage with nothing but my logo
• Simple design - stands out
Should not have
• Colour that dont align with my logo
• Over complicated '/ non symmetrical design

```html
<!DOCTYPE html>
<html lang="en">
<head>
<meta charset="utf-8">
<title>Dalvik Ostrander Photography – Business Card</title>
<link href="https://fonts.googleapis.com/css2?family=Cinzel:wght@400;600&family=Lato:wght@400&display=swap" rel="stylesheet">
<style>
  :root {
    --backdrop: #e9e6e1;
    --card-top: #1c1c1c;
    --card-bottom: #272727;
    --gold: #8c7b5f;
    --gold-soft: #9a8a6e;
    --mark-fill: rgba(140, 123, 95, 0.16);
  }
  * { margin: 0; padding: 0; box-sizing: border-box; }
  html, body {
    width: 1200px;
    height: 443px;
    overflow: hidden;
    background: var(--backdrop);
  }
  .canvas {
    position: relative;
    width: 1200px;
    height: 443px;
  }
  .card {
    position: absolute;
    top: 91px;
    width: 478px;
    height: 272px;
    border-radius: 14px;
    background: linear-gradient(180deg, var(--card-top), var(--card-bottom));
    box-shadow: 0 2px 4px rgba(0, 0, 0, 0.25);
    overflow: hidden;
  }
  .card--front { left: 108px; }
  .card--back { left: 609px; }

  .monogram-area {
    position: absolute;
    background: var(--mark-fill);
  }
  .card--front .monogram-area--large {
    left: 360px;
    top: 6px;
    width: 118px;
    height: 256px;
    border-radius: 40px 0 0 40px;
  }
  .card--back .monogram-area--large {
    left: 0;
    top: 6px;
    width: 121px;
    height: 256px;
    border-radius: 0 40px 40px 0;
  }
  .monogram-area--logo {
    left: 263px;
    top: 61px;
    width: 96px;
    height: 98px;
    border-radius: 10px;
  }

  .contact {
    position: absolute;
    left: 172px;
    top: 88px;
  }
  .contact__name {
    font-family: "Cinzel", serif;
    font-weight: 600;
    font-size: 16px;
    line-height: 22px;
    letter-spacing: 2.5px;
    color: var(--gold);
    margin-bottom: 4px;
  }
  .contact__list { list-style: none; }
  .contact__item {
    display: flex;
    align-items: center;
    gap: 8px;
    height: 20px;
    font-family: "Lato", sans-serif;
    font-size: 12.5px;
    color: var(--gold-soft);
  }
  .contact__icon {
    width: 11px;
    height: 11px;
    flex: none;
  }

  .brand {
    position: absolute;
    left: 111px;
    width: 400px;
    top: 170px;
    text-align: center;
    font-family: "Cinzel", serif;
    font-weight: 400;
    color: var(--gold);
  }
  .brand__name {
    display: block;
    font-size: 20px;
    letter-spacing: 0.5px;
    line-height: 22px;
  }
  .brand__trade {
    display: block;
    font-size: 9px;
    letter-spacing: 5.5px;
    line-height: 14px;
  }
</style>
</head>
<body>
<main class="canvas">
  <section class="card card--front" aria-label="Card front">
    <div class="monogram-area monogram-area--large" role="img" aria-label="Large decorative monogram, left half, in muted gold"></div>
    <div class="contact">
      <p class="contact__name">Your Name</p>
      <ul class="contact__list">
        <li class="contact__item">
          <svg class="contact__icon" viewBox="0 0 12 12" aria-hidden="true">
            <path d="M1 4c0-2 2-3 5-3s5 1 5 3v1H8.5V4h-5v1H1z M3 6h6l1.5 5h-9z" fill="var(--gold-soft)"/>
          </svg>
          Phone Number
        </li>
        <li class="contact__item">
          <svg class="contact__icon" viewBox="0 0 12 12" aria-hidden="true">
            <g fill="none" stroke="var(--gold-soft)" stroke-width="1">
              <circle cx="6" cy="6" r="5"/>
              <ellipse cx="6" cy="6" rx="2.2" ry="5"/>
              <line x1="1" y1="6" x2="11" y2="6"/>
            </g>
          </svg>
          tavorelstudio.com
        </li>
        <li class="contact__item">
          <svg class="contact__icon" viewBox="0 0 12 12" aria-hidden="true">
            <rect x="0.5" y="2.5" width="11" height="7" fill="var(--gold-soft)"/>
            <path d="M0.5 2.5 6 6.5 11.5 2.5" fill="none" stroke="var(--card-top)" stroke-width="1"/>
          </svg>
          Email Address
        </li>
      </ul>
    </div>
  </section>

  <section class="card card--back" aria-label="Card back">
    <div class="monogram-area monogram-area--large" role="img" aria-label="Large decorative monogram, right half, in muted gold"></div>
    <div class="monogram-area monogram-area--logo" role="img" aria-label="Studio logo mark in muted gold"></div>
    <p class="brand">
      <span class="brand__name">Dalvik Ostrander</span>
      <span class="brand__trade">Photography</span>
    </p>
  </section>
</main>
</body>
</html>
```